Advertise property management capabilities for Staylume short term rentals

Infographic that describes steps for researching property, Signing Lease with property, Prepare property, List property on Staylume, Manage guests lifecycle (book - Stay), including collecting booking revenue. We are using the infographic to market to property managers to demonstrate how converting existing properties to Staylume will increase profitability

Target Market(s)

Property Managers, Real Estate agents

Industry/Entity Type

Property Management

Requirements
Must have
• finished product will be used on back of business cards as well as flyer, used in email marketing, web site
Nice to have
• works with Staylume logo color

```html
<!DOCTYPE html>
<html lang="en">
<head>
<meta charset="utf-8">
<title>5 Steps for increasing profitability with Staylume</title>
<link rel="stylesheet" href="https://fonts.googleapis.com/css2?family=Montserrat:wght@300;500;600;700&display=swap">
<style>
  :root {
    --bg: #ebebeb;
    --red: #f05663;
    --red-dark: #d94250;
    --grey: #5e5e5e;
    --grey-dark: #474747;
    --green: #5faa1e;
    --green-dark: #4a8b12;
    --blue: #45b8f2;
    --blue-dark: #2f8fca;
    --line: #4a4a4a;
    --maroon: #8f1f2a;
    --white: #ffffff;
    --sky: #d9d9d9;
    --sky-deep: #b9b9b9;
  }
  html, body { margin: 0; padding: 0; }
  body {
    width: 1200px; height: 2723px; overflow: hidden;
    background: var(--bg); position: relative;
    font-family: "Montserrat", sans-serif;
  }
  .artwork { position: absolute; left: 0; top: 0; }
  .header-title {
    position: absolute; left: 490px; top: 20px; margin: 0;
    font-weight: 300; font-size: 142px; line-height: 1; color: var(--white);
    letter-spacing: -2px;
  }
  .header-subtitle {
    position: absolute; left: 498px; top: 204px; margin: 0;
    font-weight: 600; font-size: 39px; line-height: 49px; color: var(--maroon);
  }
  .brand-name { color: var(--white); }
  .step-label {
    position: absolute; left: 554px; margin: 0;
    font-weight: 500; font-size: 31px; line-height: 42px; color: var(--white);
  }
  .cycle-label {
    position: absolute; margin: 0; color: var(--white);
    font-weight: 500; font-size: 26px; line-height: 36px; white-space: nowrap;
  }
  .cycle-label-booking { left: 499px; top: 2044px; }
  .cycle-label-stay { left: 838px; top: 1970px; }
  .cycle-label-money { left: 818px; top: 2246px; }
  .cycle-label-prepare { left: 518px; top: 2238px; width: 170px; text-align: center; }
  .number { font-family: "Montserrat", sans-serif; font-weight: 700; font-size: 54px; }
</style>
</head>
<body>
<svg class="artwork" width="1200" height="2723" viewBox="0 0 1200 2723" xmlns="http://www.w3.org/2000/svg">
  <defs>
    <linearGradient id="band-red" x1="0" y1="0" x2="0" y2="1">
      <stop offset="0.5" stop-color="var(--red)"/><stop offset="0.5" stop-color="var(--red-dark)"/>
    </linearGradient>
    <linearGradient id="band-grey" x1="0" y1="0" x2="0" y2="1">
      <stop offset="0.5" stop-color="var(--grey)"/><stop offset="0.5" stop-color="var(--grey-dark)"/>
    </linearGradient>
    <linearGradient id="band-green" x1="0" y1="0" x2="0" y2="1">
      <stop offset="0.5" stop-color="var(--green)"/><stop offset="0.5" stop-color="var(--green-dark)"/>
    </linearGradient>
    <linearGradient id="band-blue" x1="0" y1="0" x2="0" y2="1">
      <stop offset="0.5" stop-color="var(--blue)"/><stop offset="0.5" stop-color="var(--blue-dark)"/>
    </linearGradient>
    <linearGradient id="skyline-fill" x1="0" y1="0" x2="0" y2="1">
      <stop offset="0" stop-color="var(--sky)"/><stop offset="1" stop-color="var(--sky-deep)"/>
    </linearGradient>
    <linearGradient id="house-fill" x1="0" y1="0" x2="1" y2="0">
      <stop offset="0.5" stop-color="#444"/><stop offset="0.5" stop-color="#555"/>
    </linearGradient>
  </defs>

  <rect class="skyline" x="0" y="2140" width="1200" height="583" fill="url(#skyline-fill)" role="img" aria-label="Grey city skyline silhouette"/>

  <path class="header-panel" d="M109 0 H1102 V394 Q1102 414 1082 414 H129 Q109 414 109 394 Z" fill="var(--red)"/>
  <circle class="header-emblem" cx="294" cy="203" r="160" fill="url(#house-fill)" role="img" aria-label="Red house with a tree on a green lawn"/>

  <line x1="172" y1="584" x2="172" y2="1739" stroke="var(--line)" stroke-width="5"/>

  <g class="step step-research">
    <line x1="216" y1="584" x2="330" y2="584" stroke="var(--line)" stroke-width="5"/>
    <rect x="480" y="493" width="610" height="182" rx="91" fill="none" stroke="var(--red)" stroke-width="10"/>
    <rect x="480" y="521" width="582" height="126" rx="63" fill="url(#band-red)"/>
    <circle cx="412" cy="584" r="98" fill="var(--white)"/>
    <circle cx="412" cy="584" r="88" fill="var(--red)"/>
    <g fill="none" stroke="var(--white)" stroke-width="6" stroke-linecap="round" stroke-linejoin="round">
      <circle cx="398" cy="570" r="40"/>
      <line x1="427" y1="599" x2="462" y2="634"/>
      <path d="M378 572 L398 552 L418 572 M384 566 V590 H412 V566"/>
    </g>
    <circle cx="172" cy="584" r="42" fill="var(--white)" stroke="var(--red)" stroke-width="9"/>
    <text class="number" x="172" y="603" text-anchor="middle" fill="var(--red)">1</text>
  </g>

  <g class="step step-lease">
    <line x1="216" y1="875" x2="330" y2="875" stroke="var(--line)" stroke-width="5"/>
    <rect x="480" y="784" width="610" height="182" rx="91" fill="none" stroke="var(--grey)" stroke-width="10"/>
    <rect x="480" y="812" width="582" height="126" rx="63" fill="url(#band-grey)"/>
    <circle cx="412" cy="875" r="98" fill="var(--white)"/>
    <circle cx="412" cy="875" r="88" fill="var(--grey)"/>
    <g fill="none" stroke="var(--white)" stroke-width="6" stroke-linecap="round" stroke-linejoin="round">
      <rect x="372" y="822" width="76" height="100" rx="6"/>
      <line x1="388" y1="848" x2="432" y2="848"/>
      <line x1="388" y1="866" x2="432" y2="866"/>
      <line x1="388" y1="884" x2="418" y2="884"/>
      <circle cx="448" cy="912" r="14"/>
      <path d="M440 924 L436 942 L448 936 L460 942 L456 924"/>
    </g>
    <circle cx="172" cy="875" r="42" fill="var(--white)" stroke="var(--grey)" stroke-width="9"/>
    <text class="number" x="172" y="894" text-anchor="middle" fill="var(--grey)">2</text>
  </g>

  <g class="step step-prepare">
    <line x1="216" y1="1162" x2="330" y2="1162" stroke="var(--line)" stroke-width="5"/>
    <rect x="480" y="1071" width="610" height="182" rx="91" fill="none" stroke="var(--green)" stroke-width="10"/>
    <rect x="480" y="1099" width="582" height="126" rx="63" fill="url(#band-green)"/>
    <circle cx="412" cy="1162" r="98" fill="var(--white)"/>
    <circle cx="412" cy="1162" r="88" fill="var(--green)"/>
    <g fill="none" stroke="var(--white)" stroke-width="6" stroke-linecap="round" stroke-linejoin="round">
      <rect x="362" y="1112" width="82" height="34" rx="8"/>
      <path d="M444 1129 H458 V1164 H404 V1182"/>
      <rect x="396" y="1182" width="16" height="36" rx="4"/>
      <path d="M375 1160 Q370 1172 375 1178 Q382 1172 375 1160 Z"/>
      <path d="M446 1188 V1204 M438 1196 H454"/>
    </g>
    <circle cx="172" cy="1162" r="42" fill="var(--white)" stroke="var(--green)" stroke-width="9"/>
    <text class="number" x="172" y="1181" text-anchor="middle" fill="var(--green)">3</text>
  </g>

  <g class="step step-listing">
    <line x1="216" y1="1452" x2="330" y2="1452" stroke="var(--line)" stroke-width="5"/>
    <rect x="480" y="1361" width="610" height="182" rx="91" fill="none" stroke="var(--blue)" stroke-width="10"/>
    <rect x="480" y="1389" width="582" height="126" rx="63" fill="url(#band-blue)"/>
    <circle cx="412" cy="1452" r="98" fill="var(--white)"/>
    <circle cx="412" cy="1452" r="88" fill="var(--blue)"/>
    <g fill="none" stroke="var(--white)" stroke-width="6" stroke-linecap="round" stroke-linejoin="round">
      <rect x="352" y="1404" width="120" height="80" rx="5"/>
      <line x1="352" y1="1420" x2="472" y2="1420"/>
      <rect x="366" y="1432" width="30" height="14"/>
      <rect x="366" y="1456" width="30" height="14"/>
      <line x1="406" y1="1439" x2="458" y2="1439"/>
      <line x1="406" y1="1463" x2="458" y2="1463"/>
      <path d="M402 1484 V1500 M422 1484 V1500 M388 1502 H436"/>
    </g>
    <circle cx="172" cy="1452" r="42" fill="var(--white)" stroke="var(--blue)" stroke-width="9"/>
    <text class="number" x="172" y="1471" text-anchor="middle" fill="var(--blue)">4</text>
  </g>

  <g class="step step-guests">
    <line x1="216" y1="1739" x2="330" y2="1739" stroke="var(--line)" stroke-width="5"/>
    <rect x="480" y="1648" width="610" height="182" rx="91" fill="none" stroke="var(--red)" stroke-width="10"/>
    <rect x="480" y="1676" width="582" height="126" rx="63" fill="url(#band-red)"/>
    <circle cx="412" cy="1739" r="98" fill="var(--white)"/>
    <circle cx="412" cy="1739" r="88" fill="var(--red)"/>
    <g fill="none" stroke="var(--white)" stroke-linecap="round">
      <circle cx="396" cy="1724" r="28" stroke-width="14" stroke-dasharray="9 7"/>
      <circle cx="396" cy="1724" r="12" stroke-width="6"/>
      <circle cx="442" cy="1768" r="18" stroke-width="11" stroke-dasharray="7 6"/>
      <circle cx="442" cy="1768" r="6" stroke-width="5"/>
    </g>
    <circle cx="172" cy="1739" r="42" fill="var(--white)" stroke="var(--red)" stroke-width="9"/>
    <text class="number" x="172" y="1758" text-anchor="middle" fill="var(--red)">5</text>
  </g>

  <line x1="729" y1="1834" x2="729" y2="1880" stroke="var(--line)" stroke-width="5"/>
  <g class="cycle" stroke="var(--bg)" stroke-width="8">
    <path d="M445.4 2106.6 A290 290 0 0 1 781.4 1871.4 L749.2 2053.6 A105 105 0 0 0 627.6 2138.8 Z" fill="var(--red)"/>
    <path d="M781.4 1871.4 A290 290 0 0 1 1016.6 2207.4 L834.4 2175.2 A105 105 0 0 0 749.2 2053.6 Z" fill="var(--green)"/>
    <path d="M1016.6 2207.4 A290 290 0 0 1 680.6 2442.6 L712.8 2260.4 A105 105 0 0 0 834.4 2175.2 Z" fill="var(--blue)"/>
    <path d="M680.6 2442.6 A290 290 0 0 1 445.4 2106.6 L627.6 2138.8 A105 105 0 0 0 712.8 2260.4 Z" fill="var(--grey)"/>
  </g>
  <circle cx="731" cy="2157" r="104" fill="var(--white)"/>
  <g fill="none" stroke="var(--grey-dark)" stroke-width="5" stroke-linecap="round" stroke-linejoin="round">
    <path d="M666 2140 L731 2092 L796 2140"/>
    <path d="M682 2210 V2168 H774 V2210 M682 2192 H774"/>
    <rect x="692" y="2150" width="30" height="18" rx="4"/>
    <rect x="734" y="2150" width="30" height="18" rx="4"/>
    <path d="M720 2124 L728 2132 L744 2116"/>
  </g>
  <g fill="none" stroke="var(--white)" stroke-width="5" stroke-linecap="round" stroke-linejoin="round">
    <rect x="612" y="1946" width="90" height="78" rx="6"/>
    <line x1="612" y1="1966" x2="702" y2="1966"/>
    <line x1="632" y1="1938" x2="632" y2="1952"/>
    <line x1="682" y1="1938" x2="682" y2="1952"/>
    <path d="M895 2110 L940 2065 M930 2075 L942 2087 M918 2087 L930 2099"/>
    <path d="M890 2140 Q920 2130 960 2140"/>
    <circle cx="895" cy="2360" r="18"/>
    <path d="M848 2344 H876 M848 2358 H872 M848 2372 H874"/>
    <path d="M502 2190 L532 2164 L562 2190 M510 2184 V2214 H554 V2184"/>
  </g>
</svg>

<h1 class="header-title">5 STEPS</h1>
<p class="header-subtitle">for increasing profitability<br>by converting<br>your property to <span class="brand-name">Staylume</span></p>

<p class="step-label" style="top:563px">Property Research Report</p>
<p class="step-label" style="top:833px">Sign Lease to allow<br>Short Term Rental</p>
<p class="step-label" style="top:1141px">Prepare property</p>
<p class="step-label" style="top:1431px">List property on Staylume</p>
<p class="step-label" style="top:1718px">Manage guests lifecycle</p>

<p class="cycle-label cycle-label-booking">Guest<br>Booking</p>
<p class="cycle-label cycle-label-stay">Guest<br>Stay</p>
<p class="cycle-label cycle-label-money">Collect<br>money</p>
<p class="cycle-label cycle-label-prepare">Prepare<br>property for<br>next Guest</p>
</body>
</html>
```